Communication Business Card Design

We offer complete cabling solutions
Data Cabling,Fibre Optic, and Cabling Repairs fault finding
Security camera installation
TV Aerial installation
Security alarm installation
HWR

Industry/Entity Type

Business

Contact Information for Business Card

Brightmoor Solutions
ABN 58 214 992 367
EMAIL brightmoorsolutions.com.au
Mobile 0491236057
Lou Archer

```html
<!DOCTYPE html>
<html lang="en">
<head>
<meta charset="utf-8">
<title>Brightmoor Solutions – Business Card</title>
<link rel="stylesheet" href="https://fonts.googleapis.com/css2?family=Zilla+Slab:wght@400;600&family=Montserrat:wght@700&display=swap">
<style>
  :root {
    --page-bg: #e4e4e4;
    --photo-deep: #0b1f5c;
    --photo-mid: #2a56b8;
    --photo-bright: #5fa8ee;
    --photo-cyan: #2fd3f0;
    --panel-navy: #0c2a57;
    --panel-border: #b7cfa4;
    --panel-light: #b9d1ea;
    --ink-navy: #0f2447;
    --text-white: #f4f6fb;
    --bullet-green: #a9c79a;
  }
  * { box-sizing: border-box; margin: 0; padding: 0; }
  html, body {
    width: 1200px;
    height: 1000px;
    overflow: hidden;
    background: var(--page-bg);
  }
  .card {
    position: absolute;
    left: 280px;
    width: 640px;
    height: 370px;
    overflow: hidden;
    box-shadow: 0 6px 18px rgba(0,0,0,0.25);
  }
  .card--back { top: 110px; }
  .card--front { top: 520px; }

  .card__photo {
    position: absolute;
    inset: 0;
  }
  .card--back .card__photo {
    background:
      radial-gradient(circle at 70% 35%, rgba(180,110,230,0.55), transparent 35%),
      linear-gradient(120deg, var(--photo-bright) 0%, var(--photo-mid) 35%, var(--photo-deep) 70%, #13306e 100%);
  }
  .card--front .card__photo {
    background:
      radial-gradient(circle at 85% 30%, rgba(47,211,240,0.6), transparent 30%),
      radial-gradient(circle at 60% 10%, rgba(220,235,255,0.6), transparent 18%),
      linear-gradient(135deg, #3d5f9e 0%, var(--photo-deep) 45%, #071033 65%, var(--photo-mid) 100%);
  }

  .services-panel {
    position: absolute;
    left: 48px;
    top: 102px;
    width: 356px;
    height: 280px;
    background: var(--panel-navy);
    border: 2px solid var(--panel-border);
    border-radius: 40px 40px 0 0;
    padding: 22px 20px 0 24px;
  }
  .services-list {
    list-style: none;
    font-family: "Zilla Slab", serif;
    font-size: 19px;
    line-height: 28px;
    color: var(--text-white);
  }
  .services-list li::before {
    content: "";
    display: inline-block;
    width: 8px;
    height: 8px;
    margin-right: 7px;
    border-radius: 50%;
    background: var(--bullet-green);
    vertical-align: 2px;
  }

  .contact-panel {
    position: absolute;
    left: 58px;
    top: 112px;
    width: 372px;
    height: 270px;
    background: var(--panel-light);
    border: 2px solid #e8f0f8;
    border-radius: 40px 40px 0 0;
    padding: 40px 0 0 30px;
    color: var(--ink-navy);
  }
  .company-name {
    font-family: "Montserrat", sans-serif;
    font-weight: 700;
    font-size: 21px;
    letter-spacing: 1.2px;
    text-transform: uppercase;
  }
  .contact-details {
    margin-top: 34px;
    font-family: "Zilla Slab", serif;
    font-size: 19px;
    line-height: 24px;
  }
  .contact-details .abn { padding-left: 16px; }
  .contact-details .icon {
    display: inline-block;
    width: 16px;
    text-align: center;
    margin-right: 4px;
    font-size: 16px;
  }
  .contact-details svg { vertical-align: -3px; }
  .contact-name {
    margin-top: 34px;
    padding-left: 30px;
    font-family: "Zilla Slab", serif;
    font-weight: 600;
    font-size: 19px;
  }
</style>
</head>
<body>

<section class="card card--back">
  <div class="card__photo" role="img" aria-label="Photo of blue network cables plugged into a numbered patch panel"></div>
  <div class="services-panel">
    <ul class="services-list">
      <li>Complete cabling solutions</li>
      <li>Data Cabling,</li>
      <li>Fault finding</li>
      <li>Security camera installation</li>
      <li>TV Aerial installation</li>
      <li>Security alarm installation</li>
      <li>Fibre Optic and Cabling Repairs</li>
      <li>HWR</li>
    </ul>
  </div>
</section>

<section class="card card--front">
  <div class="card__photo" role="img" aria-label="Photo collage of network cables, glowing fibre optics and binary data streams"></div>
  <div class="contact-panel">
    <h1 class="company-name">Brightmoor Solutions</h1>
    <div class="contact-details">
      <p class="abn">ABN 58 214 992 367</p>
      <p><span class="icon">@</span>brightmoorsolutions.com.au</p>
      <p><span class="icon"><svg width="12" height="18" viewBox="0 0 12 18"><rect x="1" y="1" width="10" height="16" rx="1.5" fill="none" stroke="currentColor" stroke-width="1.6"/><rect x="3" y="3" width="6" height="5" fill="currentColor"/><circle cx="6" cy="13.5" r="1.2" fill="currentColor"/></svg></span>Mobile&nbsp; 0491236057</p>
    </div>
    <p class="contact-name">Lou Archer</p>
  </div>
</section>

</body>
</html>
```